Casa Vero Inspections Business Card

I need a business card for my new company. The company is going to provide home inspections. The name of the company is Casa Vero Inspections. I am not sure if I want a single sided card or a double. I have a logo already that I want to incorporate into the card design. I was wondering if I should incorporate a catch phrase on my card or not. If I did the phrase would be "The Intelligent Choice for Home Inspections" but i am unsure how or if to use it on a card. The following information needs to be on the card.
Home Inspection
My Name: Marcus T. Wolford Phone Number: 555-301-7762 Email: mwolford@casaveroinspections.com Website: www.casaveroinspections.com NY HI License # 27300519462

```html
<!DOCTYPE html>
<html lang="en">
<head>
<meta charset="utf-8">
<title>Casa Vero Inspections – Business Card</title>
<link rel="stylesheet" href="https://fonts.googleapis.com/css2?family=Montserrat:wght@700&family=Arimo:wght@400&display=swap">
<style>
  :root {
    --backdrop: #2b2b2d;
    --card: #1d1d1f;
    --accent: #6cc3ee;
    --ink: #ffffff;
    --ink-soft: #e6e6e6;
  }
  * { box-sizing: border-box; margin: 0; padding: 0; }
  html, body {
    width: 1200px; height: 900px; overflow: hidden;
    background: var(--backdrop);
  }
  .canvas {
    width: 1200px; height: 900px;
    display: flex; flex-direction: column;
    align-items: center; justify-content: center; gap: 50px;
  }
  .card {
    width: 630px; height: 360px;
    background: var(--card);
    position: relative;
    box-shadow: 0 10px 30px rgba(0,0,0,.45);
  }
  .wordmark {
    display: flex; align-items: center; gap: 12px;
    font-family: "Montserrat", sans-serif; font-weight: 700;
    color: var(--ink); text-transform: uppercase; letter-spacing: 1px;
    line-height: 1.05;
  }
  .wordmark__square {
    width: 18px; height: 18px; background: var(--accent); flex: none;
  }
  /* Front */
  .card--front {
    display: flex; flex-direction: column; align-items: center; justify-content: center;
  }
  .card--front .wordmark { font-size: 34px; margin-top: 20px; }
  .tagline {
    font-family: "Arimo", sans-serif; font-size: 15px; color: var(--ink-soft);
    margin-top: 70px; letter-spacing: .3px;
  }
  /* Back */
  .card--back { display: flex; align-items: center; }
  .card--back .brand {
    width: 320px; display: flex; justify-content: center; padding-top: 40px;
  }
  .card--back .wordmark { font-size: 26px; }
  .divider {
    width: 1px; height: 190px; background: var(--accent); flex: none;
  }
  .contact {
    padding-left: 40px; font-family: "Arimo", sans-serif; color: var(--ink);
  }
  .contact__name {
    font-family: "Montserrat", sans-serif; font-weight: 700;
    font-size: 20px; color: var(--accent);
  }
  .contact__title { font-size: 14px; margin-top: 2px; }
  .contact__license { font-size: 14px; margin-top: 26px; }
  .contact__list { list-style: none; margin-top: 20px; font-size: 14px; }
  .contact__list li { display: flex; align-items: center; gap: 8px; margin-top: 6px; }
  .contact__list svg { width: 12px; height: 12px; fill: var(--accent); flex: none; }
</style>
</head>
<body>
<main class="canvas">
  <section class="card card--front">
    <div class="wordmark"><span class="wordmark__square"></span>Casa Vero<br>Inspections</div>
    <p class="tagline">The Intelligent Choice for Home Inspections</p>
  </section>

  <section class="card card--back">
    <div class="brand">
      <div class="wordmark"><span class="wordmark__square"></span>Casa Vero<br>Inspections</div>
    </div>
    <div class="divider"></div>
    <div class="contact">
      <h1 class="contact__name">Marcus T. Wolford</h1>
      <p class="contact__title">CEO/Founder</p>
      <p class="contact__license">NY HI License # 27300519462</p>
      <ul class="contact__list">
        <li>
          <svg viewBox="0 0 24 24" aria-hidden="true"><path d="M6.6 10.8a15 15 0 0 0 6.6 6.6l2.2-2.2c.3-.3.7-.4 1-.2 1.1.4 2.3.6 3.6.6.6 0 1 .4 1 1V20c0 .6-.4 1-1 1C10.6 21 3 13.4 3 4c0-.6.4-1 1-1h3.5c.6 0 1 .4 1 1 0 1.3.2 2.5.6 3.6.1.3 0 .7-.2 1z"/></svg>
          555-301-7762
        </li>
        <li>
          <svg viewBox="0 0 24 24" aria-hidden="true"><path d="M2 5h20v14H2z M2 5l10 8 10-8" fill="none" stroke="#6cc3ee" stroke-width="2"/></svg>
          mwolford@casaveroinspections.com
        </li>
        <li>
          <svg viewBox="0 0 24 24" aria-hidden="true"><path d="M12 2a10 10 0 1 0 0 20 10 10 0 0 0 0-20zm0 2c1 0 2.4 2.2 2.8 6H9.2C9.6 6.2 11 4 12 4zm-2.8 8h5.6c-.4 3.8-1.8 6-2.8 6s-2.4-2.2-2.8-6zM4.1 12h3.1c.1 2.3.6 4.3 1.3 5.6A8 8 0 0 1 4.1 12zm0-2a8 8 0 0 1 4.4-5.6C7.8 5.7 7.3 7.7 7.2 10zm12.7 2h3.1a8 8 0 0 1-4.4 5.6c.7-1.3 1.2-3.3 1.3-5.6zm0-2c-.1-2.3-.6-4.3-1.3-5.6A8 8 0 0 1 19.9 10z"/></svg>
          www.casaveroinspections.com
        </li>
      </ul>
    </div>
  </section>
</main>
</body>
</html>
```